LANDING PAGE on a Word Press platform.

I have a website, www.thecalmledgermerchant.com and need to create a new landing page. I purchased a new url, www.calmledgermerchant.com and set it up on Word Press. It has a theme (I was trying to do it myself, but gave up) but you can change it if you need to. I will give you access so you can work directly on the Word Press Platform. Please visit my site, www.thecalmledgermerchant, so you can see what we are selling.
Updates

Thank you for being so patient. Unfortunately I had some pressing personal problems and had to leave the country for a couple of weeks. I am back now and will choose a design today. Thank you again!

Target Market(s)

Stock Market, High Worth Individuals, Traders, Investors

Requirements
Must have
• My landing page must look very professional and rich. I am sending a copy of my logo but the "the" before The Calm Ledger Merchant, needs to be removed. Some testimonials and services we provide. (all found on my home page)
Nice to have
• I am open to a new color scheme if possible. The logo colors would have to be changed.
Should not have
• Should not be too busy with too many images or text. I want a clean and easy to read landing page

```html
<!DOCTYPE html>
<html lang="en">
<head>
<meta charset="utf-8">
<title>The Calm Ledger Merchant</title>
<link href="https://fonts.googleapis.com/css2?family=Signika:wght@400;600&family=Open+Sans:wght@400;600&family=Oswald:wght@400;500&display=swap" rel="stylesheet">
<style>
:root{
  --gold:#b5850f;
  --gold-dark:#a0700a;
  --brown:#5a3a05;
  --navy:#1c1c52;
  --navy-title:#2b2f6b;
  --blue-band:#14148a;
  --text:#555;
  --text-dark:#222;
  --hero-bg:#ececec;
  --footer-bg:#efefef;
  --bottom:#222;
  --line:#ddd;
}
*{margin:0;padding:0;box-sizing:border-box}
html,body{width:749px;height:1200px;overflow:hidden;background:#fff}
body{position:relative;font-family:"Open Sans",sans-serif;color:var(--text)}
.abs{position:absolute}
.topbar{left:0;top:0;width:749px;height:29px;background:var(--gold)}
.toplinks{right:62px;top:8px;font-size:9px;color:#fff;word-spacing:2px}
.toplinks span{margin:0 6px}
.brand{left:64px;top:42px;display:flex;align-items:center;gap:8px}
.brand-dot{width:40px;height:40px;border-radius:50%;background:var(--navy)}
.brand-name{font-family:"Signika",sans-serif;font-weight:600;font-size:19px;line-height:20px;color:var(--gold)}
.follow{left:348px;top:62px;font-size:7px;color:var(--gold);font-weight:600}
.follow-dot{top:60px;width:15px;height:15px;border-radius:50%;background:#d4d4d4}
.hdr-divider{left:476px;top:48px;width:1px;height:38px;background:var(--line)}
.contact{right:62px;font-size:12px;color:#444;text-align:right}
.contact b{font-weight:400;color:var(--gold)}
.nav{left:0;top:104px;width:749px;height:30px;background:var(--navy)}
.nav-active{left:62px;top:104px;width:69px;height:30px;background:var(--gold)}
.nav-item{top:116px;font-size:8px;color:#fff;transform:translateX(-50%);white-space:nowrap;letter-spacing:.3px}
.hero{left:0;top:134px;width:749px;height:252px;background:var(--hero-bg)}
.hero-art{left:350px;top:134px;width:399px;height:252px;background:linear-gradient(160deg,#f4f4f4,#dcdcdc 70%,#c9c9c9)}
.hero-title{left:63px;top:184px;font-family:"Signika",sans-serif;font-weight:600;font-size:23px;line-height:33px;color:var(--navy-title)}
.hero-title span{color:var(--gold)}
.hero-text{left:64px;top:257px;width:282px;font-size:9.6px;line-height:16px;color:#666}
.dot{top:332px;width:9px;height:9px;border-radius:50%;background:#ccc}
.feature{top:406px;width:143px;height:72px;border:1px solid #ddd;background:#fff;box-shadow:0 1px 2px rgba(0,0,0,.08)}
.feature svg{position:absolute;left:50%;top:10px;transform:translateX(-50%)}
.feature-label{position:absolute;left:0;right:0;top:48px;text-align:center;font-family:"Signika",sans-serif;font-size:13px;color:var(--gold);letter-spacing:.3px}
.rule{left:62px;top:489px;width:625px;height:1px;background:var(--line)}
.section-title{top:506px;font-family:"Signika",sans-serif;font-size:15px;color:var(--gold);letter-spacing:.2px}
.welcome{left:63px;top:532px;width:421px;font-size:8.8px;line-height:15.8px;color:#555;text-align:justify}
.welcome p+p{margin-top:5px}
.chart{left:98px;top:674px;width:348px;height:216px;border:1px solid #ccc;background:#fff}
.services{left:500px;top:531px;width:187px;height:142px;background:#f5f5f5;border:1px solid #e6e6e6}
.svc{position:absolute;left:13px;font-size:9px;line-height:16px;color:#666}
.svc strong{display:block;font-weight:400;color:var(--text-dark);font-size:9.6px}
.promo{left:498px;width:189px;color:#fff;text-align:center;font-family:"Oswald",sans-serif}
.promo-free{top:686px;height:81px;background:radial-gradient(ellipse at center,#8a5d0c 40%,#5b3b04 100%)}
.promo-paid{top:788px;height:99px;background:radial-gradient(ellipse at center,#1515a0 40%,#0a0a45 100%)}
.band{left:62px;top:908px;width:625px;height:68px;background:radial-gradient(ellipse at center,#1a1aa0 30%,#0c0c60 100%);color:#fff;font-family:"Oswald",sans-serif}
.footer{left:0;top:997px;width:749px;height:165px;background:var(--footer-bg)}
.foot-title{top:1012px;font-family:"Signika",sans-serif;font-size:11.5px;color:var(--gold-dark)}
.foot-list{list-style:none;font-size:9px;color:#444;line-height:19px}
.foot-div{top:1020px;width:1px;height:120px;background:#e0e0e0}
.field{left:353px;width:153px;height:17px;background:#e4e4e4;border-radius:2px;font-size:8px;color:#555;padding:3px 9px}
.btn{left:446px;top:1123px;width:60px;height:18px;background:var(--brown);color:#fff;font-family:"Signika",sans-serif;font-weight:600;font-size:8.5px;text-align:center;line-height:18px;border-radius:2px}
.soc{left:600px;width:17px;height:17px;border-radius:50%;background:#666}
.soc-label{left:627px;font-size:9px;color:#444}
.bottom{left:0;top:1162px;width:749px;height:38px;background:var(--bottom);text-align:center;font-size:8.5px;line-height:38px;color:#888}
</style>
</head>
<body>

<div class="abs topbar"></div>
<div class="abs toplinks">Subscribe<span>|</span>Login<span>|</span>Logout</div>

<div class="abs brand"><div class="brand-dot"></div><div class="brand-name">Calm Ledger<br>Merchant</div></div>
<div class="abs follow">FOLLOW US :</div>
<div class="abs follow-dot" style="left:393px"></div>
<div class="abs follow-dot" style="left:412px"></div>
<div class="abs follow-dot" style="left:430px"></div>
<div class="abs follow-dot" style="left:448px"></div>
<div class="abs hdr-divider"></div>
<div class="abs contact" style="top:48px">Tel:&nbsp; <b>555-014-2290</b></div>
<div class="abs contact" style="top:68px">Email:&nbsp; <b>info@calmledgermerchant.com</b></div>

<div class="abs nav"></div>
<div class="abs nav-active"></div>
<div class="abs nav-item" style="left:97px">HOME</div>
<div class="abs nav-item" style="left:160px">ABOUT</div>
<div class="abs nav-item" style="left:255px">CURRENT PORTFOLIO</div>
<div class="abs nav-item" style="left:367px">LATEST REPORT</div>
<div class="abs nav-item" style="left:462px">WATCH LIST</div>
<div class="abs nav-item" style="left:553px">DAILY TICKER</div>
<div class="abs nav-item" style="left:650px">MARKET NEWS</div>

<div class="abs hero"></div>
<div class="abs hero-art" role="img" aria-label="Businessman drawing business charts, icons and a city skyline on a wall under hanging lamps"></div>
<h1 class="abs hero-title">Combining Fundamental<br><span>and Technical Analysis</span></h1>
<p class="abs hero-text">Our Team of Researchers, Stock Traders and Contributors would like to welcome you to "The Calm Ledger Merchant", an opportunity to receive research and opinions on companies and stocks that will outperform the market!!</p>
<div class="abs dot" style="left:67px;background:#f08a1c"></div>
<div class="abs dot" style="left:80px"></div>
<div class="abs dot" style="left:92px"></div>

<div class="abs feature" style="left:68px">
  <svg width="30" height="28" viewBox="0 0 30 28"><rect x="9" y="2" width="12" height="6" rx="2" fill="none" stroke="#d99a10" stroke-width="2.5"/><rect x="1" y="7" width="28" height="20" rx="3" fill="#e3a415"/></svg>
  <div class="feature-label">PORTFOLIO</div>
</div>
<div class="abs feature" style="left:225px">
  <svg width="30" height="28" viewBox="0 0 30 28"><rect x="2" y="1" width="26" height="19" rx="1" fill="none" stroke="#c98a0c" stroke-width="3"/><rect x="12" y="20" width="6" height="4" fill="#c98a0c"/><rect x="7" y="24" width="16" height="3" fill="#c98a0c"/></svg>
  <div class="feature-label">LATEST REPORT</div>
</div>
<div class="abs feature" style="left:382px">
  <svg width="30" height="30" viewBox="0 0 30 30"><path d="M15 1a13 13 0 1 1-9 22l-4 6 1-8A13 13 0 0 1 15 1z" fill="#e3a415"/><circle cx="15" cy="14" r="7" fill="none" stroke="#fff" stroke-width="1.3"/><path d="M8 14h14M15 7v14M10 10h10M10 18h10" stroke="#fff" stroke-width="1"/></svg>
  <div class="feature-label">DAILY TICKER</div>
</div>
<div class="abs feature" style="left:538px">
  <svg width="30" height="30" viewBox="0 0 30 30"><path d="M20 3l7 7L11 26H4v-7z" fill="#e3a415"/><path d="M4 19l7 7" stroke="#fff" stroke-width="1.5"/></svg>
  <div class="feature-label">WATCH LIST</div>
</div>

<div class="abs rule"></div>

<h2 class="abs section-title" style="left:63px">WELCOME TO THE CALM LEDGER MERCHANT</h2>
<div class="abs welcome">
  <p>Dear Investor,</p>
  <p>Our Team of Researchers, Stock Traders and Contributors would like to welcome you to "The Calm Ledger Merchant", an opportunity to receive research and opinions on companies and stocks that will outperform the market!!<br>If you are an investor or stock trader looking for high quality investment ideas with strong fundamentals to support them, look no further than the "The Calm Ledger Merchant" If you are an investor or stock trader looking for high quality investment ideas with strong fundamentals</p>
</div>

<div class="abs chart">
  <svg width="348" height="216" viewBox="0 0 348 216" font-family="Open Sans, sans-serif">
    <text x="175" y="17" text-anchor="middle" font-size="10" font-weight="600" fill="#111">Performance of TCLM Portfolios vs. Major Indices</text>
    <g font-size="7" fill="#333" text-anchor="end">
      <text x="22" y="11">155</text><text x="22" y="36">145</text><text x="22" y="61">135</text><text x="22" y="86">125</text><text x="22" y="111">115</text><text x="22" y="136">105</text><text x="22" y="161">95</text>
    </g>
    <rect x="27" y="6" width="309" height="155" fill="none" stroke="#999" stroke-width=".8"/>
    <polyline fill="none" stroke="#c0282d" stroke-width="1.6" points="30,146 45,152 60,148 75,146 90,144 105,146 120,142 135,140 150,138 165,134 180,127 195,120 210,118 225,96 240,90 255,88 270,92 290,60 300,38 310,42 325,36 336,34 340,34"/>
    <polyline fill="none" stroke="#1e2a6a" stroke-width="1.6" points="30,148 45,150 60,146 75,144 90,142 105,144 120,138 135,134 150,130 165,128 180,130 195,126 210,124 225,128 240,130 255,130 270,124 290,112 300,120 310,118 325,108 336,116 340,114"/>
    <polyline fill="none" stroke="#222" stroke-width="1.4" points="30,148 45,156 60,150 75,152 90,148 105,146 120,150 135,150 150,146 165,148 180,150 195,146 210,146 225,148 240,146 255,148 270,142 290,140 300,132 310,138 325,140 336,144 340,144"/>
    <polyline fill="none" stroke="#8a8a8a" stroke-width="1.2" points="30,150 45,156 60,152 75,154 90,150 105,150 120,152 135,152 150,148 165,150 180,152 195,148 210,148 225,150 240,148 255,150 270,146 290,146 300,140 310,144 325,144 336,148 340,148"/>
    <polyline fill="none" stroke="#9a70c0" stroke-width="1.2" points="30,152 45,158 60,154 75,156 90,152 105,152 120,154 135,154 150,150 165,152 180,154 195,150 210,150 225,152 240,150 255,152 270,148 290,148 300,142 310,146 325,146 336,150 340,150"/>
    <g font-size="6.5" fill="#333">
      <text transform="translate(32,172) rotate(-50)" text-anchor="end">1/1/2015</text>
      <text transform="translate(57,172) rotate(-50)" text-anchor="end">1/8/2015</text>
      <text transform="translate(82,172) rotate(-50)" text-anchor="end">1/15/2015</text>
      <text transform="translate(107,172) rotate(-50)" text-anchor="end">1/22/2015</text>
      <text transform="translate(132,172) rotate(-50)" text-anchor="end">1/29/2015</text>
      <text transform="translate(157,172) rotate(-50)" text-anchor="end">2/5/2015</text>
      <text transform="translate(182,172) rotate(-50)" text-anchor="end">2/12/2015</text>
      <text transform="translate(207,172) rotate(-50)" text-anchor="end">2/19/2015</text>
      <text transform="translate(232,172) rotate(-50)" text-anchor="end">2/26/2015</text>
      <text transform="translate(257,172) rotate(-50)" text-anchor="end">3/5/2015</text>
      <text transform="translate(282,172) rotate(-50)" text-anchor="end">3/12/2015</text>
      <text transform="translate(307,172) rotate(-50)" text-anchor="end">3/19/2015</text>
      <text transform="translate(332,172) rotate(-50)" text-anchor="end">3/26/2015</text>
    </g>
    <g font-size="6.5" fill="#333">
      <line x1="30" y1="205" x2="44" y2="205" stroke="#1e2a6a" stroke-width="1.6"/><text x="46" y="207">Current Portfolio</text>
      <line x1="110" y1="205" x2="124" y2="205" stroke="#c0282d" stroke-width="1.6"/><text x="126" y="207">Tweeted Trades</text>
      <line x1="186" y1="205" x2="200" y2="205" stroke="#8a8a8a" stroke-width="1.4"/><text x="202" y="207">Index 500</text>
      <line x1="240" y1="205" x2="254" y2="205" stroke="#9a70c0" stroke-width="1.4"/><text x="256" y="207">Blue 30</text>
      <line x1="288" y1="205" x2="302" y2="205" stroke="#222" stroke-width="1.4"/><text x="304" y="207">Tech Comp</text>
    </g>
  </svg>
</div>

<h2 class="abs section-title" style="left:499px">OUR SERVICES</h2>
<svg class="abs" style="left:673px;top:510px" width="6" height="8" viewBox="0 0 6 8"><path d="M1 1l3 3-3 3" fill="none" stroke="#888" stroke-width="1.5"/></svg>
<div class="abs services">
  <div class="svc" style="top:13px"><strong>Daily Email Updates on Current Positions</strong>Private Chirper Feed for Traderseget<br>porta urna. Feed for Traderseget</div>
  <div class="svc" style="top:79px"><strong>TCLM 15 Fab Index</strong>Weekly Report on New Recommendations<br>Live Feed on Market News</div>
</div>

<div class="abs promo promo-free">
  <div style="margin-top:13px;font-size:23px;font-weight:500;letter-spacing:2px;line-height:26px">FREE</div>
  <div style="font-size:17px;line-height:24px">2 Week Trail</div>
</div>
<div class="abs promo promo-paid">
  <div style="margin-top:17px;font-size:15.5px;line-height:23px">Become a Paid SUBSCRIBER<br>Monthly subscription<br>$150.00</div>
</div>

<div class="abs band">
  <div class="abs" style="left:23px;top:13px;font-size:26px;font-weight:500;line-height:34px">Subscribe now:</div>
  <div class="abs" style="left:210px;top:17px;font-size:20px;line-height:30px">Start a 2-Week Free Trial Today!</div>
  <svg class="abs" style="left:549px;top:14px" width="45" height="40" viewBox="0 0 45 40"><path d="M0 12h24V0l21 20-21 20V28H0z" fill="#fff"/></svg>
</div>

<div class="abs footer"></div>
<h3 class="abs foot-title" style="left:61px">Quick Links</h3>
<h3 class="abs foot-title" style="left:193px">Support Links</h3>
<h3 class="abs foot-title" style="left:352px">Newsletters Sign Up</h3>
<h3 class="abs foot-title" style="left:600px">Connect With Us</h3>
<div class="abs foot-div" style="left:155px"></div>
<div class="abs foot-div" style="left:305px"></div>
<div class="abs foot-div" style="left:552px"></div>
<ul class="abs foot-list" style="left:65px;top:1044px"><li>Home</li><li>About</li><li>Current Portfolio</li><li>Latest Report</li><li>Watchlist</li></ul>
<ul class="abs foot-list" style="left:195px;top:1046px"><li>Daily Ticker</li><li>Market News</li><li>Disclaimer</li><li>Privacy policy</li><li>Company registration</li></ul>
<p class="abs" style="left:353px;top:1040px;width:160px;font-size:9px;line-height:12px;color:#444">Sign up for our daily email by entering your information below</p>
<div class="abs field" style="top:1072px">Your name</div>
<div class="abs field" style="top:1097px">Email address</div>
<div class="abs btn">SUBSCRIBE</div>
<div class="abs soc" style="top:1043px"></div><div class="abs soc-label" style="top:1045px">Circlebook</div>
<div class="abs soc" style="top:1064px"></div><div class="abs soc-label" style="top:1066px">Chirper</div>
<div class="abs soc" style="top:1085px"></div><div class="abs soc-label" style="top:1087px">WorkLink</div>
<div class="abs soc" style="top:1106px"></div><div class="abs soc-label" style="top:1108px">Orbit+</div>

<div class="abs bottom">Copyright &copy; 2015&nbsp; calmledgermerchant.&nbsp; All rights reserved.</div>

</body>
</html>
```